Business Card Design

We need a business card design for a new company based in Melbourne Australia. We are financial broker in finance industry. We provide a wide range of finance solutions to our clients including home loans, commercial loans, business facilities, car loans, equipment loans, invoice finance, etc. The company name is from director's personal name. We would like to have a new company logo that includes TK.

Industry/Entity Type

Business

Contact Information for Business Card

company name: TK & Co Finance Pty Ltd
person's name: Desmond Okafor
role: Managing Director
Mobile: 0417 638 294
fax: 03 9561 4472
Email: desmond.okafor@tkcolending.example
Address: Suite 5/418 Marlow Avenue Elmvale Vic 3174
Credit Licence No.: 718249

```html
<!DOCTYPE html>
<html lang="en">
<head>
<meta charset="utf-8">
<title>TK &amp; Co Finance – Business Card</title>
<link rel="stylesheet" href="https://fonts.googleapis.com/css2?family=Oswald:wght@400&family=Roboto:wght@400;700&display=swap">
<style>
  :root {
    --page: #f3f4f6;
    --white: #ffffff;
    --navy: #0c2a4f;
    --blue-deep: #0a3a7a;
    --blue-bright: #1f6fd6;
    --ink: #1b1f24;
    --ink-soft: #2b2f36;
    --brand-green: #2fb54a;
    --swoosh: #c9ccd2;
  }
  * { box-sizing: border-box; margin: 0; padding: 0; }
  html, body {
    width: 1200px; height: 1200px; overflow: hidden;
    background: var(--page);
  }
  .card {
    position: absolute;
    left: 222px;
    width: 756px;
    height: 450px;
    background: var(--blue-deep);
    box-shadow: 0 28px 30px -18px rgba(0,0,0,0.35);
    overflow: hidden;
  }
  .card--front { top: 101px; }
  .card--back { top: 619px; }
  .card__bg { position: absolute; inset: 0; width: 100%; height: 100%; }

  /* Front */
  .brand {
    position: absolute; left: 0; right: 0; top: 120px;
    text-align: center;
    font-family: "Roboto", sans-serif;
    color: var(--ink);
  }
  .brand__mark {
    display: inline-flex; align-items: center; gap: 14px;
    font-family: "Roboto", sans-serif; font-weight: 700;
    font-size: 56px; color: var(--brand-green); letter-spacing: 1px;
  }
  .brand__dot {
    width: 30px; height: 30px; border-radius: 50%;
    background: var(--brand-green);
  }
  .brand__name {
    margin-top: 44px;
    font-size: 20px; font-weight: 400;
  }
  .brand__web {
    margin-top: 10px;
    font-size: 14px; font-weight: 700;
  }

  /* Back */
  .person {
    position: absolute; left: 95px; top: 40px;
    text-align: center;
  }
  .person__name {
    font-family: "Oswald", sans-serif; font-weight: 400;
    font-size: 52px; line-height: 1.1; color: var(--ink);
    letter-spacing: 1px;
  }
  .person__role {
    margin-top: 8px;
    font-family: "Roboto", sans-serif; font-weight: 700;
    font-size: 20px; color: var(--ink);
  }
  .contacts {
    position: absolute; left: 38px; top: 180px;
    list-style: none;
    font-family: "Roboto", sans-serif; font-size: 24px;
    color: var(--ink-soft);
  }
  .contacts__item {
    display: flex; align-items: center; gap: 12px;
    height: 54px;
  }
  .contacts__icon {
    width: 26px; height: 26px; border-radius: 50%;
    background: var(--navy);
    display: flex; align-items: center; justify-content: center;
    flex: none;
  }
  .contacts__icon svg { width: 14px; height: 14px; fill: var(--white); }
  .contacts__label { font-weight: 700; }
</style>
</head>
<body>

<section class="card card--front" aria-label="Business card front">
  <svg class="card__bg" viewBox="0 0 756 450" preserveAspectRatio="none" aria-hidden="true">
    <defs>
      <linearGradient id="frontBlue" x1="0" y1="0" x2="1" y2="1">
        <stop offset="0" stop-color="#1f6fd6"/>
        <stop offset="0.5" stop-color="#0a3a7a"/>
        <stop offset="1" stop-color="#062448"/>
      </linearGradient>
    </defs>
    <rect width="756" height="450" fill="url(#frontBlue)"/>
    <path d="M70,0 C40,140 30,300 110,450 L120,450 C50,300 55,140 82,0 Z" fill="#c9ccd2"/>
    <path d="M82,0 L500,0 C640,40 700,200 690,450 L120,450 C55,300 55,140 82,0 Z" fill="#ffffff"/>
    <path d="M500,0 C650,50 712,220 700,450 L690,450 C700,200 640,40 500,0 Z" fill="#c9ccd2"/>
  </svg>
  <div class="brand">
    <div class="brand__mark"><span class="brand__dot"></span>TK</div>
    <p class="brand__name">TK &amp; Co Finance Pty Ltd</p>
    <p class="brand__web">www.tkcolending.example</p>
  </div>
</section>

<section class="card card--back" aria-label="Business card back">
  <svg class="card__bg" viewBox="0 0 756 450" preserveAspectRatio="none" aria-hidden="true">
    <defs>
      <linearGradient id="backBlue" x1="0" y1="0" x2="1" y2="1">
        <stop offset="0" stop-color="#062448"/>
        <stop offset="0.5" stop-color="#0a3a7a"/>
        <stop offset="1" stop-color="#1f6fd6"/>
      </linearGradient>
    </defs>
    <rect width="756" height="450" fill="url(#backBlue)"/>
    <path d="M0,0 L470,0 C640,70 730,250 740,450 L0,450 Z" fill="#c9ccd2"/>
    <path d="M0,0 L450,0 C620,60 715,250 722,450 L0,450 Z" fill="#ffffff"/>
  </svg>

  <div class="person">
    <h1 class="person__name">Desmond Okafor</h1>
    <p class="person__role">Managing Director</p>
  </div>

  <ul class="contacts">
    <li class="contacts__item">
      <span class="contacts__icon"><svg viewBox="0 0 16 16"><path d="M4 1h3l1 4-2 1c1 2 2 3 4 4l1-2 4 1v3c0 1-1 2-2 2C7 14 2 9 2 3c0-1 1-2 2-2z"/></svg></span>
      <span><span class="contacts__label">Phone:</span> 0417 638 294</span>
    </li>
    <li class="contacts__item">
      <span class="contacts__icon"><svg viewBox="0 0 16 16"><path d="M4 1h7v4H4zM2 6h12v6h-2v3H4v-3H2zM5 10v3h6v-3z"/></svg></span>
      <span><span class="contacts__label">Fax:</span> 03 9561 4472</span>
    </li>
    <li class="contacts__item">
      <span class="contacts__icon"><svg viewBox="0 0 16 16"><path d="M1 3h14v10H1zM2 4l6 5 6-5v1L8 10 2 5z"/></svg></span>
      <span><span class="contacts__label">Email:</span> desmond.okafor@tkcolending.example</span>
    </li>
    <li class="contacts__item">
      <span class="contacts__icon"><svg viewBox="0 0 16 16"><path d="M8 1a5 5 0 0 1 5 5c0 4-5 9-5 9S3 10 3 6a5 5 0 0 1 5-5zm0 3a2 2 0 1 0 0 4 2 2 0 0 0 0-4z"/></svg></span>
      <span>Suite 5/418 Marlow Avenue Elmvale Vic 3174</span>
    </li>
    <li class="contacts__item">
      <span class="contacts__icon"><svg viewBox="0 0 16 16"><path d="M2 3h12v10H2zM4 6h5v1H4zm0 3h8v1H4z"/></svg></span>
      <span><span class="contacts__label">Credit Licence No.:</span> 718249</span>
    </li>
  </ul>
</section>

</body>
</html>
```